The Busy Wren Organic & Natural Soaps is looking for label designs (along with the business card proje

This is my scope and requirements:
Labelling project:
This is related to the Label project I also opened up. (The Busy Wren Organic & Natural Soaps needs a good business card (Contest) )
I have attached an initial draft at a logo I tried to come up with for a business card and labelling/marketing. I am hoping that you can take this logo and 'run with it' to finesse it, make it look unique and professional. If you need to change it, I am open to ideas.
I find that labelling/packaging is hard for me to make it look 'professional' so I am coming to the experts!
I am looking for label designs for 2 different bottles and 2 different bar soaps:
1) Organic Bar Soap (2 possibilities: 1) Kraft 'cigar' band around soap with twine, 2) Kraft soap box with Kraft sticker Labels
2) Natural Olive Oil Based Bar Soap (labelling can be same as Organic but with distinct info)
3) Organic Hand Washes (clear square bottles, 250ml with natural pump)
4) Natural Olive Oil Based Body Wash (taper bottle 200ml with metal silver disc top caps)
I am a start up at home company making Organic and Natural Bar soaps, hand soaps, body washes.
All of my ingredients are organic or natural and will include natural essential oils, exfoliants, natural powders/colours, etc.
Some of the names are: Brisquel (feisty, energetic soap), Dunmoor (more of a sandalwood earthy tones with a sandalwood powder exfoliant), Frosk (maybe changing this name - fresh scented), Plum Cardamom (lemongrass/ginger, exfoliants), etc....
If you need more information, please let me know!
Please find attached: Kraft Paper I am looking at to possibly wrap the Bar Soaps in (I like the different colour concept and am trying to decide between diff colours of Wendell Prask paper to wrap around or plain kraft paper.. whichever the new logo concept will look best with.
The bottles I will be using for the hand soap (250ml square) and the body wash (200ml tapered)
OLD POST:
Hello! I am a start up business that is specializing in making luxury organic bar soaps, natural olive oil bar soaps, organic hand wash, natural olive oil body wash/shower gel that will include essential oils, exfoliants, natural powders, etc. (also accessories: wood soap dishes, etc) .. I am looking for a great designer that can provide me with the business card and labelling designs! I appreciate feedback, ideas on how I can receive a great design to help sell my products!
I am attaching my initial logo design that I would like to keep - but am looking for someone to 'finesse' it or make it more professional/unique looking.
Again, this is hand in hand with the business card project I submitted.
Thanks!
Mirela
Updates
I am sorry for the lack of direction or Scope of the project. I am new at this board.
Labelling project:
I have attached an initial draft at a logo I tried to come up with for a business card and labelling/marketing. I am hoping that you can take this logo and 'run with it' to finesse it, make it look unique and professional.
If you need more information, please let me know.
Hello; I just wanted to let everyone know that if you feel that this brand needs a different logo, I am open to ideas (if you don't think the one I started with is ok). I am coming to the experts here!
Just to confirm also - this is related to the business card project, therefore, there are 2 projects, 2 payments! :)
Cheers

```html
<!DOCTYPE html>
<html lang="en">
<head>
<meta charset="utf-8">
<title>The Busy Wren – Brisquel Hand Wash Label</title>
<link href="https://fonts.googleapis.com/css2?family=Short+Stack&family=Special+Elite&display=swap" rel="stylesheet">
<style>
  :root {
    --page-bg: #ffffff;
    --label-cream: #ebe3d3;
    --label-cream-light: #f3eee4;
    --band-pink: #cf92d0;
    --ink-grey: #77787a;
    --ink-white: #ffffff;
    --side-text: rgba(255, 255, 255, 0.75);
  }
  * { box-sizing: border-box; margin: 0; padding: 0; }
  html, body {
    width: 1200px;
    height: 1000px;
    overflow: hidden;
    background: var(--page-bg);
  }
  .canvas {
    position: relative;
    width: 1200px;
    height: 1000px;
  }
  .label {
    position: absolute;
    left: 320px;
    top: 150px;
    width: 560px;
    height: 700px;
    background: linear-gradient(180deg, var(--label-cream-light) 0%, var(--label-cream) 100%);
    overflow: hidden;
  }
  .label__side-text {
    position: absolute;
    top: 50%;
    width: 680px;
    text-align: center;
    font-family: "Short Stack", cursive;
    font-size: 30px;
    letter-spacing: 2px;
    color: var(--side-text);
    white-space: nowrap;
  }
  .label__side-text--left {
    left: 28px;
    transform: translate(-50%, -50%) rotate(-90deg);
  }
  .label__side-text--right {
    right: 28px;
    transform: translate(50%, -50%) rotate(90deg);
  }
  .label__band {
    position: absolute;
    left: 170px;
    top: 0;
    width: 220px;
    height: 420px;
    background: var(--band-pink);
  }
  .brand {
    position: absolute;
    left: 170px;
    top: 80px;
    width: 220px;
    display: flex;
    flex-direction: column;
    align-items: center;
    gap: 16px;
  }
  .brand__dot {
    width: 110px;
    height: 110px;
    border-radius: 50%;
    background: var(--ink-grey);
  }
  .brand__name {
    font-family: "Short Stack", cursive;
    font-size: 21px;
    line-height: 1.3;
    text-align: center;
    color: var(--ink-grey);
  }
  .product {
    position: absolute;
    left: 0;
    top: 430px;
    width: 100%;
    text-align: center;
    color: var(--ink-grey);
    font-family: "Short Stack", cursive;
  }
  .product__name {
    font-size: 38px;
    font-weight: 400;
    line-height: 1.2;
  }
  .product__tagline {
    font-size: 18px;
    margin-top: 2px;
  }
  .label__spec {
    position: absolute;
    left: 170px;
    top: 548px;
    width: 220px;
    height: 132px;
    background: var(--band-pink);
    padding: 34px 0 0 22px;
    font-family: "Special Elite", monospace;
    font-size: 20px;
    line-height: 1.3;
    color: var(--ink-white);
  }
</style>
</head>
<body>
  <main class="canvas">
    <section class="label">
      <p class="label__side-text label__side-text--left">100% organic earth friendly pure</p>
      <p class="label__side-text label__side-text--right">100% organic earth friendly pure</p>

      <div class="label__band"></div>

      <div class="brand">
        <span class="brand__dot"></span>
        <p class="brand__name">The Busy Wren<br>Organic &amp;<br>Natural Soaps</p>
      </div>

      <div class="product">
        <h1 class="product__name">Brisquel</h1>
        <p class="product__tagline">feisty, energetic soap</p>
      </div>

      <div class="label__spec">
        250ML<br>ORGANIC<br>HAND WASH
      </div>
    </section>
  </main>
</body>
</html>
```